passmarlo.com

Develop a website for passmarlo.com will be a site to sell tickets for concerts, shows, shows, theaters and others. I need a web design easy view, very easy to use and accumulate events by date. The aim is to develop the site was connected to a complex system that is already developed. (Important this page to a robust system was connected via links the idea is to develop only the front view)
Updates

Reason: I need more designs yet we have not made the decision

Target Market(s)

millennials, adults, who want to enjoy concerts and shows

Industry/Entity Type

Event

Number of Pages Required

5+ page

Colors
1b1b1b
aaaaaa
ffffff

Requirements
Must have
• Easy Vista, accumulation of upcoming events, past events. The tabs should have are: 1 Start: In this part of upcoming events occur. You could put a banner on the top and down the events by date. 2. How to order: page with instructions on how to purchase tickets 3. About Us: The company history 4. Contact: Phones and template for contact by mail 5. Our policies: shopping 6. Notice Privacy: Privacy Notice Copoy 7. Centers Sale: physical places where they can purchase tickets Promoters 8. access: Link to a template
Nice to have
• as you can see p www.fondarivent.com or entravú.com or pasuqo.com or gatelorvi.com (important this page to a robust system was connected via links the idea is to develop only the front view)
Should not have
• Many things Tangled

```html
<!DOCTYPE html>
<html lang="en">
<head>
<meta charset="utf-8">
<title>Passmarlo — Buy Tickets for Concerts &amp; Shows</title>
<link rel="stylesheet" href="https://fonts.googleapis.com/css2?family=Montserrat:wght@400;500;600&family=Open+Sans:wght@400;600&display=swap">
<style>
:root{
  --ink:#1b1b1b;
  --grey:#aaaaaa;
  --white:#ffffff;
  --footer:#e4e4e4;
  --muted:#555555;
  --date-box:rgba(170,170,170,.85);
  --caption:rgba(0,0,0,.88);
}
*{margin:0;padding:0;box-sizing:border-box}
html,body{width:705px;height:1200px;overflow:hidden;background:var(--white)}
body{position:relative;font-family:"Open Sans",Arial,sans-serif;color:var(--ink)}

.site-header{position:absolute;left:0;top:0;width:705px;height:57px;background:var(--ink)}
.brand{position:absolute;left:69px;top:17px;font-family:"Montserrat",Arial,sans-serif;font-weight:600;font-size:18px;letter-spacing:.5px;color:var(--white)}
.main-nav{position:absolute;left:216px;top:0;display:flex;height:57px;align-items:center}
.main-nav a{position:relative;color:var(--white);text-decoration:none;font-size:9px;padding:0 6px;font-family:"Open Sans",Arial,sans-serif}
.main-nav a.is-active::before{content:"";position:absolute;left:0;right:0;top:-26px;height:3px;background:var(--white)}

.hero{position:absolute;left:0;top:57px;width:705px;height:323px}
.hero-photo{position:absolute;inset:0;background:
  radial-gradient(ellipse at 55% 15%,rgba(200,150,255,.85),rgba(120,70,170,.5) 35%,transparent 65%),
  linear-gradient(180deg,#5a3a78 0%,#3a2440 45%,#1a1014 100%)}
.hero-text{position:absolute;left:70px;top:92px;color:var(--white)}
.hero-title{font-family:"Montserrat",Arial,sans-serif;font-weight:500;line-height:1.05}
.hero-title .line-1{display:block;font-size:22px}
.hero-title .line-2{display:block;font-size:26px}
.hero-lede{margin-top:6px;font-size:9.5px;line-height:12px;width:300px}
.btn-book{position:absolute;left:78px;top:181px;width:107px;height:29px;border:1.5px solid var(--white);color:var(--white);font-family:"Montserrat",Arial,sans-serif;font-size:8px;font-weight:600;display:flex;align-items:center;justify-content:center;text-decoration:none}
.slider-dots{position:absolute;left:318px;top:301px;display:flex;gap:3px}
.slider-dots span{width:14px;height:2px;background:var(--white)}
.slider-dots span.is-dim{background:rgba(255,255,255,.45)}

.events-title{position:absolute;left:0;top:406px;width:705px;text-align:center;font-family:"Montserrat",Arial,sans-serif;font-weight:500;font-size:19px;letter-spacing:.5px}

.event-card{position:absolute;overflow:hidden;color:var(--white)}
.event-photo{position:absolute;inset:0}
.event-caption{position:absolute;left:0;right:0;bottom:0;height:46px;background:var(--caption);display:flex;align-items:center}
.event-date{width:42px;height:46px;background:var(--date-box);display:flex;flex-direction:column;align-items:center;justify-content:center;font-family:"Montserrat",Arial,sans-serif;line-height:1}
.event-date .day{font-size:18px}
.event-date .month{font-size:10px;margin-top:3px}
.event-info{padding-left:8px;flex:1}
.event-name{font-family:"Montserrat",Arial,sans-serif;font-size:12.5px;font-weight:500}
.event-summary{font-size:9px;margin-top:2px}
.event-arrow{width:20px;height:46px;display:flex;align-items:center;justify-content:center}

.more-events{position:absolute;left:331px;top:1068px}

.site-footer{position:absolute;left:0;top:1114px;width:705px;height:86px;background:var(--footer)}
.footer-nav{position:absolute;left:70px;top:25px;display:flex}
.footer-nav a{font-size:8px;color:var(--muted);text-decoration:none;padding:0 6px}
.copyright{position:absolute;left:76px;top:42px;font-size:7.5px;color:var(--muted)}
.social{position:absolute;left:547px;top:25px;display:flex;gap:3px}
.social span{width:20px;height:20px;border:1.5px solid var(--ink);border-radius:50%}
</style>
</head>
<body>

<header class="site-header">
  <div class="brand">PASSMARLO</div>
  <nav class="main-nav">
    <a class="is-active" href="#">Home</a>
    <a href="#">How to Order</a>
    <a href="#">About us</a>
    <a href="#">Contact us</a>
    <a href="#">Policies</a>
    <a href="#">Privacy</a>
    <a href="#">Center Sale</a>
    <a href="#">Access</a>
  </nav>
</header>

<section class="hero">
  <div class="hero-photo" role="img" aria-label="Concert crowd with raised hands under purple stage lights"></div>
  <div class="hero-text">
    <h1 class="hero-title"><span class="line-1">BUY TICKETS FOR</span><span class="line-2">CONCERTS &amp; SHOWS</span></h1>
    <p class="hero-lede">Ut ac mi quis lacus mollis aliquam Curabitur iaculis tempus eros Curabitur vel mi sit amet magna malesuada ultrices</p>
  </div>
  <a class="btn-book" href="#">BOOK TICKETS</a>
  <div class="slider-dots"><span></span><span></span><span class="is-dim"></span><span></span></div>
</section>

<h2 class="events-title">Upcoming Events</h2>

<a class="event-card" style="left:70px;top:451px;width:282px;height:215px" href="#">
  <div class="event-photo" role="img" aria-label="Jazz band playing saxophone and trumpet on stage" style="background:linear-gradient(135deg,#6a6e7a,#2e2a30 60%,#8a7a6a)"></div>
  <div class="event-caption"><div class="event-date"><span class="day">26</span><span class="month">MAR</span></div><div class="event-info"><div class="event-name">Event Tittle here</div><div class="event-summary">Vivamus porttitor purus nisi eleifend libero</div></div><div class="event-arrow"><svg width="8" height="13" viewBox="0 0 8 13"><path d="M1 1l5.5 5.5L1 12" fill="none" stroke="#fff" stroke-width="1.6"/></svg></div></div>
</a>
<a class="event-card" style="left:356px;top:451px;width:282px;height:215px" href="#">
  <div class="event-photo" role="img" aria-label="Drummer performing under warm stage lights" style="background:linear-gradient(135deg,#5a4a6a,#2a2228 50%,#d8a070)"></div>
  <div class="event-caption"><div class="event-date"><span class="day">28</span><span class="month">MAR</span></div><div class="event-info"><div class="event-name">Event Tittle here</div><div class="event-summary">Vivamus porttitor purus nisi eleifend libero</div></div><div class="event-arrow"><svg width="8" height="13" viewBox="0 0 8 13"><path d="M1 1l5.5 5.5L1 12" fill="none" stroke="#fff" stroke-width="1.6"/></svg></div></div>
</a>

<a class="event-card" style="left:69px;top:674px;width:187px;height:181px" href="#">
  <div class="event-photo" role="img" aria-label="Guitarist playing to a crowd in stage haze" style="background:linear-gradient(135deg,#3a2a24,#8a6a58 55%,#2a1e1a)"></div>
  <div class="event-caption"><div class="event-date"><span class="day">01</span><span class="month">APR</span></div><div class="event-info"><div class="event-name">Event Tittle here</div><div class="event-summary">Ut nisi erat fermentum vel</div></div><div class="event-arrow"><svg width="8" height="13" viewBox="0 0 8 13"><path d="M1 1l5.5 5.5L1 12" fill="none" stroke="#fff" stroke-width="1.6"/></svg></div></div>
</a>
<a class="event-card" style="left:260px;top:674px;width:187px;height:181px" href="#">
  <div class="event-photo" role="img" aria-label="Dancers in silhouette against a golden backdrop" style="background:linear-gradient(180deg,#c88a4a,#e0a860 50%,#8a5a30)"></div>
  <div class="event-caption"><div class="event-date"><span class="day">04</span><span class="month">APR</span></div><div class="event-info"><div class="event-name">Event Tittle here</div><div class="event-summary">Ut nisi erat fermentum vel</div></div><div class="event-arrow"><svg width="8" height="13" viewBox="0 0 8 13"><path d="M1 1l5.5 5.5L1 12" fill="none" stroke="#fff" stroke-width="1.6"/></svg></div></div>
</a>
<a class="event-card" style="left:450px;top:674px;width:187px;height:181px" href="#">
  <div class="event-photo" role="img" aria-label="Festival crowd under blue spotlights" style="background:linear-gradient(180deg,#8ab0d8,#3a5a88 50%,#0e1420)"></div>
  <div class="event-caption"><div class="event-date"><span class="day">15</span><span class="month">APR</span></div><div class="event-info"><div class="event-name">Event Tittle here</div><div class="event-summary">Ut nisi erat fermentum vel</div></div><div class="event-arrow"><svg width="8" height="13" viewBox="0 0 8 13"><path d="M1 1l5.5 5.5L1 12" fill="none" stroke="#fff" stroke-width="1.6"/></svg></div></div>
</a>

<a class="event-card" style="left:69px;top:861px;width:187px;height:181px" href="#">
  <div class="event-photo" role="img" aria-label="Ornate theatre auditorium with gilded balconies" style="background:linear-gradient(180deg,#a07a3a,#6a3a1a 55%,#3a1a10)"></div>
  <div class="event-caption"><div class="event-date"><span class="day">20</span><span class="month">APR</span></div><div class="event-info"><div class="event-name">Event Tittle here</div><div class="event-summary">Ut nisi erat fermentum vel</div></div><div class="event-arrow"><svg width="8" height="13" viewBox="0 0 8 13"><path d="M1 1l5.5 5.5L1 12" fill="none" stroke="#fff" stroke-width="1.6"/></svg></div></div>
</a>
<a class="event-card" style="left:260px;top:861px;width:187px;height:181px" href="#">
  <div class="event-photo" role="img" aria-label="Audience seated in a red-lit concert hall" style="background:linear-gradient(180deg,#2a1a1e,#b03030 45%,#c8a890)"></div>
  <div class="event-caption"><div class="event-date"><span class="day">22</span><span class="month">APR</span></div><div class="event-info"><div class="event-name">Event Tittle here</div><div class="event-summary">Ut nisi erat fermentum vel</div></div><div class="event-arrow"><svg width="8" height="13" viewBox="0 0 8 13"><path d="M1 1l5.5 5.5L1 12" fill="none" stroke="#fff" stroke-width="1.6"/></svg></div></div>
</a>
<a class="event-card" style="left:450px;top:861px;width:187px;height:181px" href="#">
  <div class="event-photo" role="img" aria-label="Raised hands silhouetted against warm bokeh lights" style="background:linear-gradient(135deg,#e8d0b0,#b07060 50%,#3a1e24)"></div>
  <div class="event-caption"><div class="event-date"><span class="day">23</span><span class="month">APR</span></div><div class="event-info"><div class="event-name">Event Tittle here</div><div class="event-summary">Ut nisi erat fermentum vel</div></div><div class="event-arrow"><svg width="8" height="13" viewBox="0 0 8 13"><path d="M1 1l5.5 5.5L1 12" fill="none" stroke="#fff" stroke-width="1.6"/></svg></div></div>
</a>

<svg class="more-events" width="42" height="16" viewBox="0 0 42 16" aria-label="More events"><path d="M1 1l20 14L41 1" fill="none" stroke="#bbbbbb" stroke-width="1.5"/></svg>

<footer class="site-footer">
  <nav class="footer-nav">
    <a href="#">Home</a><a href="#">How to Order</a><a href="#">About us</a><a href="#">Contact us</a><a href="#">Policies</a><a href="#">Privacy</a><a href="#">Center Sale</a><a href="#">Access</a>
  </nav>
  <p class="copyright">© 2017 Company Name&nbsp; All right reserved&nbsp; Term of Use</p>
  <div class="social" aria-label="Social links"><span></span><span></span><span></span><span></span></div>
</footer>

</body>
</html>
```